The Lanternfall Dash 35th Anniversary Poster

Design a poster for the 35th anniversary of The Lanternfall Dash, a 5K with 3,000+ participants that runs through downtown Lexington. The event graphics are heavily influenced by Bertram Holloway's The Copper Orchard Tale. Traditionally the event art keeps the same feel, with slight changes to the color or direction/look of the runners. Original PSD files are available but will not upload to Artvane.

Runners, athletes, active lifestyle

```html
<!DOCTYPE html>
<html lang="en">
<head>
<meta charset="utf-8">
<title>The Lanternfall Dash — 35th Anniversary Poster</title>
<link href="https://fonts.googleapis.com/css2?family=Exo+2:ital,wght@1,800;1,900&family=Roboto:wght@400;500&display=swap" rel="stylesheet">
<style>
  :root {
    --night-top: #0b0d35;
    --night-mid: #3b2a72;
    --dusk-glow: #a65a9e;
    --ground: #050409;
    --pink: #e6519f;
    --pink-soft: #f07bbd;
    --royal-blue: #1d4f8c;
    --navy: #13244f;
    --white: #ffffff;
    --lavender: #8e84cf;
  }
  * { margin: 0; padding: 0; box-sizing: border-box; }
  html, body { width: 800px; height: 1200px; overflow: hidden; background: var(--ground); }
  .poster {
    position: relative;
    width: 800px;
    height: 1200px;
    overflow: hidden;
    font-family: "Roboto", Arial, sans-serif;
    color: var(--white);
    background: linear-gradient(180deg,
      var(--night-top) 0%,
      #1c1a52 18%,
      var(--night-mid) 34%,
      var(--dusk-glow) 52%,
      #3a1f4e 64%,
      var(--ground) 74%,
      var(--ground) 100%);
  }
  .skyline {
    position: absolute;
    left: 0; top: 170px;
    width: 800px; height: 640px;
    background: linear-gradient(180deg, rgba(40,40,100,0.35) 0%, rgba(120,80,150,0.35) 55%, rgba(10,8,20,0.6) 100%);
  }
  .event-mark {
    position: absolute;
    left: 70px; top: 110px;
    display: flex; align-items: center; gap: 12px;
    font-family: "Roboto", Arial, sans-serif;
    font-weight: 500;
    font-size: 24px;
    line-height: 1.1;
    color: var(--pink-soft);
    width: 240px;
  }
  .event-mark .dot {
    flex: none;
    width: 26px; height: 26px;
    border-radius: 50%;
    background: var(--pink-soft);
  }
  .anniversary {
    position: absolute;
    left: 430px; top: 92px;
    width: 340px; height: 108px;
  }
  .anniversary svg { position: absolute; inset: 0; }
  .anniversary .label {
    position: absolute;
    left: 30px; top: 14px;
    font-family: "Exo 2", Arial, sans-serif;
    font-style: italic; font-weight: 900;
    font-size: 72px; line-height: 1;
    letter-spacing: -1px;
  }
  .anniversary .the { color: var(--navy); }
  .anniversary .ordinal { color: var(--pink); }
  .runner {
    position: absolute;
    left: 340px; top: 320px;
    width: 460px; height: 560px;
    background: radial-gradient(ellipse at 50% 45%, rgba(142,132,207,0.55) 0%, rgba(142,132,207,0.25) 50%, rgba(142,132,207,0) 75%);
  }
  .tale-title {
    position: absolute;
    left: 60px; top: 450px;
    font-family: "Exo 2", Arial, sans-serif;
    font-style: italic; font-weight: 900;
    line-height: 0.9;
    paint-order: stroke fill;
    -webkit-text-stroke: 7px var(--white);
  }
  .tale-title span { display: block; }
  .tale-title .line-one { font-size: 86px; color: var(--royal-blue); text-shadow: 6px 6px 0 rgba(10,10,40,0.45); }
  .tale-title .line-two { font-size: 76px; color: var(--pink); margin-left: 150px; text-shadow: 6px 6px 0 rgba(10,10,40,0.45); }
  .tale-title .line-three { font-size: 76px; color: var(--navy); margin-left: 200px; text-shadow: 6px 6px 0 var(--pink); }
  .run-title {
    position: absolute;
    left: 0; top: 740px;
    width: 800px;
    text-align: center;
  }
  .run-title .kicker {
    display: block;
    text-align: right;
    padding-right: 60px;
    font-size: 32px;
    font-weight: 400;
  }
  .run-title .name {
    display: block;
    font-size: 108px;
    font-weight: 400;
    line-height: 0.95;
    letter-spacing: -1px;
  }
  .run-title .accent {
    display: block;
    font-size: 56px;
    font-weight: 400;
    color: var(--pink);
    letter-spacing: 2px;
    margin-top: 4px;
  }
  .divider {
    position: absolute;
    left: 60px; top: 978px;
    width: 680px; height: 3px;
    background: linear-gradient(90deg, rgba(230,81,159,0) 0%, var(--pink) 50%, rgba(230,81,159,0) 100%);
  }
  .details {
    position: absolute;
    left: 0; top: 1005px;
    width: 800px;
    text-align: center;
    font-size: 32px;
    line-height: 1.25;
  }
  .details .count { color: var(--pink); }
</style>
</head>
<body>
<main class="poster">
  <div class="skyline" role="img" aria-label="Night city skyline silhouette of downtown towers"></div>

  <div class="event-mark">
    <span class="dot"></span>
    <span>The Lanternfall Dash</span>
  </div>

  <div class="anniversary">
    <svg width="340" height="108" viewBox="0 0 340 108" aria-hidden="true">
      <polygon points="14,0 340,0 326,108 0,108" fill="#ffffff"/>
      <polygon points="0,108 326,108 340,0 340,14 330,118 -4,118" fill="#13244f" opacity="0.5"/>
    </svg>
    <div class="label"><span class="the">the</span> <span class="ordinal">35th</span></div>
  </div>

  <div class="runner" role="img" aria-label="Silhouette of a sprinting runner"></div>

  <h2 class="tale-title">
    <span class="line-one">The Copper</span>
    <span class="line-two">Orchard</span>
    <span class="line-three">Tale</span>
  </h2>

  <h1 class="run-title">
    <span class="kicker">Orchard Tale</span>
    <span class="name">Lanternfall</span>
    <span class="accent">Dash</span>
  </h1>

  <div class="divider"></div>

  <p class="details">
    Lexington<br>
    <span class="count">3,000+</span> participants<br>
    that runs through downtown
  </p>
</main>
</body>
</html>
```